Redesign of the Molvekraut label

I am a pharmacist and sell a bitters called "Molvekraut". I would like to revise and modernize the current logo of my "Molvekraut". I have attached a photo of the current label. I have different bottle sizes with different label sizes, but for now I will only need one label for the 700ml size:
20ml 36x47mm
40ml 45x62mm
200ml 70x91mm
350ml 70x98mm
500ml 70x110mm
700ml 87x119mm
The Molve is a small stream that runs through our town. The Molvekraut is a play on words that takes up the mysticism of the Harz, as a spirit can of course also be a schnapps. I like the mysticism and rough nature of the Harz in connection with the product. I have attached a logo suggestion that I once had an AI design. But I am very open to new ideas. A connection to my pharmacy does not necessarily have to be recognizable. VG, K. Harmsen

Target Market(s)

End consumers, gastronomy, restaurants, hotels

```html
<!DOCTYPE html>
<html lang="de">
<head>
<meta charset="utf-8">
<title>Molvekraut – Etikett 700 ml</title>
<link rel="stylesheet" href="https://fonts.googleapis.com/css2?family=UnifrakturCook:wght@700&family=Open+Sans:wght@400;600&display=swap">
<style>
  :root{
    --paper:#ffffff;
    --brown:#633917;
    --ink-light:#ffffff;
    --gold-dark:#9a4f1f;
    --gold-mid:#d7a12e;
    --gold-light:#f1d232;
  }
  html,body{margin:0;padding:0;overflow:hidden;background:var(--paper);}
  .label-canvas{display:block;width:737px;height:1200px;}
  .blackletter{font-family:"UnifrakturCook","UnifrakturMaguntia",serif;font-weight:700;}
  .sans{font-family:"Open Sans",Arial,sans-serif;font-weight:400;}
  .ink-brown{fill:var(--brown);}
  .ink-light{fill:var(--ink-light);}
  .rule{stroke:var(--ink-light);stroke-width:1.2;}
  .panel{fill:var(--brown);}
</style>
</head>
<body>
<svg class="label-canvas" viewBox="0 0 737 1200" xmlns="http://www.w3.org/2000/svg">
  <defs>
    <linearGradient id="gold-band" x1="0" y1="0" x2="1" y2="0">
      <stop offset="0" stop-color="#a85c24"/>
      <stop offset="0.12" stop-color="#c98a2c"/>
      <stop offset="0.22" stop-color="#efd032"/>
      <stop offset="0.45" stop-color="#d39b2d"/>
      <stop offset="0.55" stop-color="#f0d332"/>
      <stop offset="0.75" stop-color="#d29a2c"/>
      <stop offset="0.9" stop-color="#8e4a1e"/>
      <stop offset="1" stop-color="#e9c530"/>
    </linearGradient>
    <linearGradient id="gold-inner" x1="0" y1="0" x2="1" y2="0">
      <stop offset="0" stop-color="#e7c233"/>
      <stop offset="0.25" stop-color="#d9a72e"/>
      <stop offset="0.5" stop-color="#f0d332"/>
      <stop offset="0.8" stop-color="#d09a2c"/>
      <stop offset="1" stop-color="#9b4f1f"/>
    </linearGradient>
    <symbol id="star" viewBox="-10 -10 20 20">
      <path d="M0,-9 L2.4,-3 L8.6,-2.8 L3.8,1.2 L5.3,7.4 L0,3.9 L-5.3,7.4 L-3.8,1.2 L-8.6,-2.8 L-2.4,-3 Z"/>
    </symbol>
    <path id="arch-line" d="M232,172 Q368,112 516,172"/>
  </defs>

  <!-- outer gold frame -->
  <path class="label-frame" fill="url(#gold-band)"
        d="M73,158 L117,158 C180,72 270,49 368,49 C466,49 556,72 619,158 L663,158 L663,1041 L619,1041 C556,1128 466,1150 368,1150 C270,1150 180,1128 117,1041 L73,1041 Z"/>
  <!-- inner gold field -->
  <path class="label-field" fill="url(#gold-inner)" stroke="#b06a26" stroke-width="1.5"
        d="M102,176 L140,176 C200,100 280,73 368,73 C456,73 536,100 596,176 L634,176 L634,1024 L596,1024 C536,1104 456,1128 368,1128 C280,1128 200,1104 140,1024 L102,1024 Z"/>
  <!-- brown body panel -->
  <path class="panel" d="M111,292 L626,292 L626,1016 L590,1016 C530,1092 452,1116 368,1116 C284,1116 206,1092 146,1016 L111,1016 Z"/>

  <!-- header -->
  <g class="header-stars ink-brown">
    <use href="#star" x="241" y="109" width="18" height="18"/>
    <use href="#star" x="293" y="93" width="18" height="18"/>
    <use href="#star" x="358" y="87" width="18" height="18"/>
    <use href="#star" x="428" y="96" width="18" height="18"/>
    <use href="#star" x="493" y="115" width="18" height="18"/>
  </g>
  <text class="blackletter ink-brown" font-size="38" text-anchor="middle">
    <textPath href="#arch-line" startOffset="50%">Bad Kellröder</textPath>
  </text>
  <text class="blackletter ink-brown" x="376" y="187" font-size="23" text-anchor="middle">erlesener</text>
  <text class="blackletter ink-brown product-title" x="168" y="262" font-size="96" textLength="415" lengthAdjust="spacingAndGlyphs">Molvekraut</text>

  <!-- description -->
  <g class="ink-light">
    <line class="rule" x1="270" y1="329" x2="294" y2="329"/>
    <line class="rule" x1="446" y1="329" x2="470" y2="329"/>
    <text class="blackletter" x="370" y="332" font-size="24" text-anchor="middle">Bitterlikör</text>
    <text class="blackletter" x="370" y="372" font-size="24" text-anchor="middle">nach alter Apothekerkunst</text>
    <g class="sans" font-size="19.5" text-anchor="middle">
      <text x="370" y="413">Eine Zubereitung nach höchst geheimem Rezept.</text>
      <text x="370" y="454">Sie sei empfohlen zum Genuss nach</text>
      <text x="370" y="495">einem guten Mahl.</text>
      <text x="370" y="536">Aufs Feinste zubereitet mit geistigen Auszügen</text>
      <text x="370" y="577">von Enzian, Kalmus, Malabar-Kardamom</text>
      <text x="370" y="618">und anderen wertvollen Zutaten.</text>
    </g>
    <line class="rule" x1="140" y1="640" x2="599" y2="640"/>
  </g>

  <!-- maker -->
  <g class="maker ink-light">
    <text class="sans" x="179" y="705" font-size="23">Aus der</text>
    <text class="blackletter" x="141" y="752" font-size="40">St. Ansgar</text>
    <text class="blackletter" x="141" y="794" font-size="40">Apotheke</text>
    <text class="blackletter" x="141" y="836" font-size="40">Bad Kellrode</text>
    <g class="sans" font-size="21">
      <text x="142" y="884">Dr. K. Harmsen</text>
      <text x="142" y="913">Lindenweg 12</text>
      <text x="142" y="942">37999 Bad Kellrode</text>
      <text x="142" y="971">Tel.: 05500-1234</text>
    </g>
  </g>

  <!-- volume and brand mark -->
  <g class="ink-light">
    <text class="sans volume" x="595" y="707" font-size="38" text-anchor="end">700ml 34% vol</text>
    <circle cx="473" cy="826" r="34" fill="none" stroke="var(--ink-light)" stroke-width="3"/>
    <text class="sans brand-name" x="473" y="898" font-size="24" text-anchor="middle" letter-spacing="2">MOLVEKRAUT</text>
  </g>

  <!-- footer -->
  <g class="ink-light">
    <line class="rule" x1="131" y1="1007" x2="599" y2="1007"/>
    <text class="sans" x="370" y="1030" font-size="16" text-anchor="middle" letter-spacing="0.5">Kräuterlikör, Chininhaltig L2313886</text>
    <use href="#star" x="232" y="1056" width="18" height="18"/>
    <use href="#star" x="298" y="1076" width="18" height="18"/>
    <use href="#star" x="368" y="1083" width="18" height="18"/>
    <use href="#star" x="432" y="1077" width="18" height="18"/>
    <use href="#star" x="486" y="1062" width="18" height="18"/>
  </g>
</svg>
</body>
</html>
```